依頼詳細
(1)ポスターの概要
ポスターは別途、A1もしくはA2で印刷し、ラミネート加工した上で、ポスター立てに設置。商店街を通る通行客に対して、①アイキャッチ(美味しいぬか漬けや惣菜などがあること)、②70年の伝統がある八百屋であること、を訴求します。つなり、(a)通行客の足を留めるインパクト、(b)足を止めた人に伝統があり、美味しい商品がある「食べてみたい!」という印象をもってもらえること、が目的です。その(a)(b)を満たすようなポスターデザインを希望します。活用方法としては、そのほかにA4サイズでPOPとして利用することも検討しています。

(2)留意点
尚、貼付写真はスマホで撮影しており、画素数がそれほど高くないことは承知しております。画素数の兼ね合いで写真の大きさなども変わってきたり、あるいは、A1で印刷する場合、粗い画像になるなどのリスクがあるかと思いますが、そのあたりも見え方によりけりかと考えますんどえ、フレキシブルに対応いただけると幸いです。

(3)お願い
①70年以上続く昔ながらの伝統ある八百屋さん、②美味しい野菜や総菜にこだわっている、③上記のこれから頑張っていこうとする3代目の意欲、などが感覚的に伝わるようなデザインを希望いたします。
記載項目
(1)社名「青果松」

(2)ショルダーネーム
北区赤羽の人々と共に歩んできた八百屋
赤羽で創業 昭和25年

(3)電話番号「03-5918-2604」

(4)キャッチコピー「70年の菌を味わう」

(5)写真
①ぬか床(貼付ファイル1枚)
②きゅうりのぬか漬け(貼付ファイル3枚)
③なすのぬか漬け(貼付ファイル1枚)
④梅干し(貼付ファイル1枚)
⑤焼き芋(貼付ファイル1枚)
⑥惣菜(貼付ファイル2枚)
⑦大根・カブのぬか漬け(貼付ファイル1枚)

・上記の①②③のどれか(良いと思われるもの)を大きく。
・その他は小さく。
・複数枚あるのは良いと思われるものを選定してください。

(6)コメント
「創業当初から、「糠は生きもの」という創業者の意思を継ぎ、
いまだに継ぎ足しながら育ててきた70年酵母の
素朴ながら深みのある味のお漬物です」
■ 選んだ理由

70年の菌を味わうというキャッチコピーを最優先に考えていただいた点、特に「70」という数字が最初に飛び込んでくる点が最も大きな選定理由です。また、黒を基調としたイメージが、歴史があるということを強調する重厚感に繋がっている点や、遠目からのアイキャッチとして機能しそうだと感じた点が選定理由として大きいです。他の作品も甲乙つけがたい部分もありましたが、最終的には当事者である青果松さんの経営陣が直感的に良いと感じたことで決定にいたりました。

■ 提案者全員のお礼・コメント

皆さま、本当にたいくさんの力作ぞろいの提案をありがとうございました。青果松の経営者からは、「どの作品も当社のことを考えてくださっていることがわかるデザインで、一つに絞りに切れない」という本音が出ていました。これからも折に触れて、ポスターをリニューアルしていきたいと考えておりますので、お付き合いの程、よろしくお願いいたします。ぜひ、店頭にいらっしゃた際には、「ポスターデザインを提案しました」と一声お声がけいただけますと幸いです。

```html
<!DOCTYPE html>
<html lang="ja">
<head>
<meta charset="utf-8">
<title>青果松 ポスター</title>
<link rel="stylesheet" href="https://fonts.googleapis.com/css2?family=Noto+Serif+JP:wght@400;600;700;900&display=swap">
<style>
  :root {
    --ink: #ffffff;
    --panel: rgba(38, 36, 34, 0.86);
    --rule: rgba(255, 255, 255, 0.75);
    --dark: #1e1c1a;
  }
  * { margin: 0; padding: 0; box-sizing: border-box; }
  html, body { width: 846px; height: 1200px; overflow: hidden; background: #222; }
  .poster {
    position: relative;
    width: 846px; height: 1200px;
    overflow: hidden;
    font-family: "Noto Serif JP", serif;
    color: var(--ink);
  }
  .photo-collage { position: absolute; inset: 0; }
  .title-panel {
    position: absolute;
    top: 0; left: 120px;
    width: 620px; height: 1200px;
    background: var(--panel);
  }
  .headline {
    position: absolute;
    left: 0; top: 30px; width: 620px; height: 780px;
    font-weight: 900;
    line-height: 1;
  }
  .headline span { position: absolute; white-space: nowrap; }
  .headline .years-number {
    left: 80px; top: 0;
    font-size: 310px; letter-spacing: -14px;
  }
  .headline .years-unit {
    left: 430px; top: 160px;
    font-size: 140px;
  }
  .headline .line {
    left: 50px;
    font-size: 176px; letter-spacing: 2px;
  }
  .headline .line-one { top: 340px; }
  .headline .line-two { top: 560px; }
  .comment {
    position: absolute; left: 0; top: 830px; width: 620px;
    text-align: center;
    font-size: 17px; line-height: 1.95; font-weight: 400;
  }
  .brand {
    position: absolute; left: 0; top: 950px; width: 620px;
    display: flex; justify-content: center; align-items: center; gap: 14px;
  }
  .brand .generation {
    border: 1.5px solid var(--ink);
    font-size: 18px; font-weight: 600;
    padding: 2px 5px;
  }
  .brand .shop-name { font-size: 56px; font-weight: 700; letter-spacing: 4px; line-height: 1.2; }
  .shoulder {
    position: absolute; left: 0; top: 1032px; width: 620px;
    display: flex; flex-direction: column; align-items: center;
  }
  .shoulder .tagline {
    width: 310px; text-align: center;
    font-size: 15px; padding: 3px 0;
    border-top: 1px solid var(--rule); border-bottom: 1px solid var(--rule);
  }
  .shoulder .founded {
    width: 310px; margin-top: 5px;
    background: var(--ink); color: var(--dark);
    text-align: center; font-size: 27px; font-weight: 900; letter-spacing: 2px;
    line-height: 1.4;
  }
  .shoulder .phone {
    width: 310px; margin-top: 4px;
    display: flex; align-items: center; justify-content: center; gap: 6px;
    font-size: 34px; font-weight: 700; letter-spacing: 1px; line-height: 1.4;
  }
</style>
</head>
<body>
<div class="poster">
  <svg class="photo-collage" width="846" height="1200" viewBox="0 0 846 1200" role="img" aria-label="ぬか床、大根・カブ・きゅうり・なすのぬか漬けの写真コラージュ">
    <defs>
      <linearGradient id="nuka-bed" x1="0" y1="0" x2="0" y2="1">
        <stop offset="0" stop-color="#6b5540"/>
        <stop offset="1" stop-color="#3b2f25"/>
      </linearGradient>
      <linearGradient id="daikon" x1="0" y1="0" x2="1" y2="0">
        <stop offset="0" stop-color="#8a7558"/>
        <stop offset="0.5" stop-color="#d8cdb8"/>
        <stop offset="1" stop-color="#a8946f"/>
      </linearGradient>
      <linearGradient id="eggplant" x1="0" y1="0" x2="0" y2="1">
        <stop offset="0" stop-color="#7a3f5a"/>
        <stop offset="1" stop-color="#3a1c2c"/>
      </linearGradient>
      <linearGradient id="cucumber" x1="0" y1="0" x2="0" y2="1">
        <stop offset="0" stop-color="#9a8466"/>
        <stop offset="0.5" stop-color="#4f5a3a"/>
        <stop offset="1" stop-color="#2a2b22"/>
      </linearGradient>
    </defs>
    <rect width="846" height="1200" fill="url(#nuka-bed)"/>
    <rect x="0" y="0" width="130" height="680" fill="url(#daikon)"/>
    <rect x="0" y="680" width="130" height="520" fill="url(#eggplant)"/>
    <rect x="730" y="0" width="116" height="1200" fill="url(#cucumber)"/>
  </svg>

  <div class="title-panel">
    <h1 class="headline" aria-label="70年の菌を味わう">
      <span class="years-number">70</span>
      <span class="years-unit">年</span>
      <span class="line line-one">の菌を</span>
      <span class="line line-two">味わう</span>
    </h1>

    <p class="comment">
      「創業当初から、「糠は生きもの」という創業者の意思を継ぎ、<br>
      いまだに継ぎ足しながら育ててきた70年酵母の<br>
      素朴ながら深みのある味のお漬物です」
    </p>

    <div class="brand">
      <span class="generation">三代目</span>
      <span class="shop-name">青果松</span>
    </div>

    <div class="shoulder">
      <p class="tagline">北区赤羽の人々と共に歩んできた八百屋</p>
      <p class="founded">赤羽で創業 昭和25年</p>
      <p class="phone">
        <svg width="30" height="26" viewBox="0 0 30 26" aria-hidden="true">
          <path d="M3 8 Q15 0 27 8 L24 12 L19 10 L19 7 Q15 5 11 7 L11 10 L6 12 Z" fill="#fff"/>
          <rect x="8" y="14" width="14" height="10" rx="2" fill="#fff"/>
        </svg>
        03-5918-2604
      </p>
    </div>
  </div>
</div>
</body>
</html>
```